Terrace Anchoring Works business card

As per your previous logo design, I would like to incorporate all those colours into the card.
I've added a business card I don't mind which is double sided. Also my Po box number..
Could be in a format so I can add new email, ph numbers etc.

Thanks

• My logo that is attached and the same colour scheme

```html
<!DOCTYPE html>
<html lang="en">
<head>
<meta charset="utf-8">
<title>Terrace Anchoring Works – Business Card</title>
<link rel="stylesheet" href="https://fonts.googleapis.com/css2?family=Arimo:wght@400;700&display=swap">
<style>
  :root {
    --page-bg: #d9d9d9;
    --card-bg: #2a2a2a;
    --card-edge: #1e1e1e;
    --accent-blue: #2ea3de;
    --text-white: #f4f4f4;
  }
  * { box-sizing: border-box; margin: 0; padding: 0; }
  html, body {
    width: 1200px;
    height: 1000px;
    overflow: hidden;
    background: var(--page-bg);
    font-family: "Arimo", Arial, sans-serif;
  }
  .sheet {
    width: 1200px;
    height: 1000px;
    display: flex;
    flex-direction: column;
    align-items: center;
    justify-content: center;
    gap: 36px;
  }
  .card {
    width: 780px;
    height: 446px;
    background: var(--card-bg);
    border: 1px solid var(--card-edge);
    box-shadow: 0 6px 18px rgba(0,0,0,0.25);
    position: relative;
  }
  .brand-name {
    color: var(--accent-blue);
    font-weight: 700;
    line-height: 1.1;
    display: flex;
    align-items: center;
    gap: 14px;
  }
  .brand-mark {
    width: 22px;
    height: 22px;
    background: var(--accent-blue);
    flex: none;
  }
  /* Front */
  .card--front {
    display: flex;
    align-items: center;
    justify-content: center;
  }
  .card--front .brand-name { font-size: 34px; }

  /* Back */
  .card--back .brand-name {
    position: absolute;
    left: 50px;
    top: 150px;
    width: 320px;
    font-size: 28px;
  }
  .contact {
    position: absolute;
    left: 430px;
    top: 62px;
    color: var(--text-white);
  }
  .contact__name {
    color: var(--accent-blue);
    font-weight: 700;
    font-size: 27px;
    letter-spacing: 0.5px;
  }
  .contact__title {
    font-size: 17px;
    margin-top: 2px;
  }
  .contact__lines {
    list-style: none;
    margin-top: 42px;
  }
  .contact__lines li {
    display: flex;
    align-items: center;
    gap: 14px;
    font-size: 19px;
    margin-bottom: 12px;
  }
  .icon {
    width: 26px;
    height: 26px;
    border-radius: 50%;
    background: var(--accent-blue);
    display: flex;
    align-items: center;
    justify-content: center;
    flex: none;
  }
  .office {
    margin-top: 34px;
    line-height: 1.2;
  }
  .office__hotline {
    color: var(--accent-blue);
    font-weight: 700;
    font-size: 19px;
  }
  .office__company {
    font-weight: 700;
    font-size: 19px;
  }
  .office__address {
    color: var(--accent-blue);
    font-size: 20px;
    font-style: normal;
  }
</style>
</head>
<body>
<main class="sheet">
  <section class="card card--front" aria-label="Card front">
    <div class="brand-name"><span class="brand-mark"></span>Terrace Anchoring Works</div>
  </section>

  <section class="card card--back" aria-label="Card back">
    <div class="brand-name"><span class="brand-mark"></span>Terrace Anchoring Works</div>

    <div class="contact">
      <p class="contact__name">YOUR NAME</p>
      <p class="contact__title">Title</p>

      <ul class="contact__lines">
        <li>
          <span class="icon">
            <svg width="14" height="14" viewBox="0 0 24 24" aria-hidden="true">
              <path fill="#2a2a2a" d="M6.6 10.8a15.1 15.1 0 0 0 6.6 6.6l2.2-2.2c.3-.3.7-.4 1-.2 1.1.4 2.3.6 3.6.6.6 0 1 .4 1 1V20c0 .6-.4 1-1 1A17 17 0 0 1 3 4c0-.6.4-1 1-1h3.5c.6 0 1 .4 1 1 0 1.3.2 2.5.6 3.6.1.3 0 .7-.2 1z"/>
            </svg>
          </span>
          0412555019
        </li>
        <li>
          <span class="icon">
            <svg width="14" height="14" viewBox="0 0 24 24" aria-hidden="true">
              <rect x="2" y="5" width="20" height="14" rx="2" fill="#2a2a2a"/>
              <path d="M3 6l9 7 9-7" fill="none" stroke="#2ea3de" stroke-width="2"/>
            </svg>
          </span>
          director@taw.com.au
        </li>
      </ul>

      <div class="office">
        <p class="office__hotline">1800 SLOPEFIX</p>
        <p class="office__company">Terrace Anchoring Works.</p>
        <address class="office__address">P.O.Box 274 Harbourvale,<br>VIC 3987</address>
      </div>
    </div>
  </section>
</main>
</body>
</html>
```